Vantrel Card

We want a business card that shows people who we are the log attached was designed by the designers on craft hive,we are using the OO in the logo (speech bubbles as our icon,so please make that part of the card ) keep the colouring the same as the logo design and we will be using high end production on the card using silver foil as the icon to make it stand out.
As Vantrel we specialise in finding influencers through social networks for brands, so if you used flimbo to comment about sports products and you were followed by of lot of users and interacted with those users then the algorithm finds you and we contact you to work for our clients as a company we then have a set of influencers that we use to support new sports products.
Also we use our algorithm to help athletes,models etc to be scored via there digital influence so when say Vorta KX ask me to find a skater that is not so much a podium rider but is more digital focused for a digital campaign then we work out who those guys or girls are to help Vorta KX
Vantrel is the name of the product and company, However I just wanted to give you the rationale of why we chose vantrel in the first place. Marbo itself is an 'abbreviation' from the proper name Alsander Wick from Tale of the Iron Hills. The character was able to look into the eskavor (sometimes translated as "Seeing Stone" but literally meaning "Farsighted" or "One that Sees from Afar") and see into the far corners of the Universe. Much in the same way as the platform has been developed is able to look into the far corners of the social network arena to help brands and Athletes will be able to see how they rated....but don't worry i don't go running around in the woods with a foam Axe and an army of dwarfs!!!
Digital Directors,Brand Directors,Athletes,Models,Celebrities and agents
Business

```html
<!DOCTYPE html>
<html lang="en">
<head>
<meta charset="utf-8">
<title>Vantrel Card</title>
<link href="https://fonts.googleapis.com/css2?family=Questrial&display=swap" rel="stylesheet">
<style>
  :root {
    --stage: #d9d9d9;
    --stage-edge: #8a8a8a;
    --brand-blue: #3fb1e3;
    --deep-blue: #1f7fae;
    --mid-blue: #3a9fd0;
    --paper: #ffffff;
    --ink: #5a5a5a;
    --ink-soft: #8b8b8b;
    --faint: #ececec;
  }
  * { box-sizing: border-box; margin: 0; padding: 0; }
  html, body { width: 1200px; height: 900px; overflow: hidden; }
  body {
    background: radial-gradient(ellipse at 55% 45%, var(--stage) 0%, #b8b8b8 60%, var(--stage-edge) 100%);
    font-family: "Questrial", "Century Gothic", sans-serif;
    position: relative;
  }
  .card {
    position: absolute;
    width: 600px;
    height: 343px;
    border-radius: 4px;
    overflow: hidden;
    box-shadow: 0 18px 40px rgba(0,0,0,.28);
  }
  /* Front */
  .card-front {
    left: 140px; top: 70px;
    background: radial-gradient(circle at 80% 15%, #5fb9e6 0%, var(--mid-blue) 35%, var(--deep-blue) 100%);
    display: flex; align-items: center; justify-content: center; gap: 22px;
  }
  .front-mark {
    width: 46px; height: 46px; border-radius: 50%;
    background: #8fd6f5;
  }
  .front-name {
    font-size: 92px; color: #8fd6f5; letter-spacing: 1px; line-height: 1;
  }
  /* Back */
  .card-back {
    left: 460px; top: 470px;
    background: var(--paper);
  }
  .back-band {
    position: absolute; left: 0; right: 0; bottom: 0; height: 22px;
    background: var(--brand-blue);
  }
  .back-tab {
    position: absolute; left: 0; bottom: 0; width: 250px; height: 62px;
    background: var(--brand-blue);
    border-top-right-radius: 10px;
    display: flex; align-items: center; padding-left: 22px;
  }
  .tab-name { color: var(--paper); font-size: 34px; line-height: 1; }
  .faint-circle {
    position: absolute; right: 60px; bottom: 8px;
    width: 170px; height: 170px; border-radius: 50%;
    background: var(--faint);
  }
  .back-wordmark {
    position: absolute; right: 36px; top: 38px;
    font-size: 72px; color: var(--brand-blue); line-height: 1; letter-spacing: 1px;
  }
  .contact { position: absolute; left: 22px; top: 22px; width: 250px; }
  .person-name { color: var(--brand-blue); font-size: 22px; letter-spacing: 1.5px; line-height: 1; }
  .person-role { color: var(--ink-soft); font-size: 9px; letter-spacing: 1.6px; text-transform: uppercase; margin: 4px 0 10px; }
  .contact-list { list-style: none; border-bottom: 1px dotted var(--ink-soft); padding-bottom: 6px; }
  .contact-list li {
    display: flex; align-items: center; gap: 8px;
    color: var(--ink); font-size: 13px; line-height: 20px;
  }
  .contact-list svg { width: 12px; height: 12px; flex: none; }
  .address { color: var(--ink); font-size: 13px; line-height: 19px; margin-top: 8px; border-bottom: 1px dotted var(--ink-soft); padding-bottom: 6px; }
</style>
</head>
<body>

<section class="card card-front" aria-label="Card front">
  <span class="front-mark" aria-hidden="true"></span>
  <span class="front-name">vantrel</span>
</section>

<section class="card card-back" aria-label="Card back">
  <div class="faint-circle" aria-hidden="true"></div>
  <div class="back-wordmark">vantrel</div>

  <div class="contact">
    <p class="person-name">DARIO VENN</p>
    <p class="person-role">Executive Creative Director</p>
    <ul class="contact-list">
      <li>
        <svg viewBox="0 0 12 12" aria-hidden="true"><path d="M3 1 L5 3.5 L4 5 Q5.5 7.5 7 8 L8.5 7 L11 9 L9.5 11 Q4 10.5 1 3 Z" fill="#7a7a7a"/></svg>
        : + 55 712-40-3318
      </li>
      <li>
        <svg viewBox="0 0 12 12" aria-hidden="true"><rect x="1" y="2.5" width="10" height="7" fill="none" stroke="#7a7a7a"/><path d="M1 2.5 L6 6.5 L11 2.5" fill="none" stroke="#7a7a7a"/></svg>
        : dario.v@vantrel.com
      </li>
      <li>
        <svg viewBox="0 0 12 12" aria-hidden="true"><circle cx="6" cy="6" r="5" fill="none" stroke="#7a7a7a"/><ellipse cx="6" cy="6" rx="2.2" ry="5" fill="none" stroke="#7a7a7a"/><path d="M1 6 H11" stroke="#7a7a7a"/></svg>
        : www.vantrel.com
      </li>
    </ul>
    <p class="address">1482 Harbor Crest Ave, South<br>Marlow Springs, United States</p>
  </div>

  <div class="back-band" aria-hidden="true"></div>
  <div class="back-tab"><span class="tab-name">vantrel</span></div>
</section>

</body>
</html>
```